Rebrand our dated accomodation business website "Tallowind Quay Residences"

we have a wordpress website ( www.tallowindquay.com.au) that is old and out dated .
I will need a new updated SQUARESPACE website (in which i already have ) with a fresh new design , also new logo and an easy site to manage from my end.
Need to connect our socials - facebook and instagram and our new site
Check out "brindle cove landing" for inspiration...
These apartments are consists of -
-One bedroom One bath
-Two bedroom One bath
-Two bedroom Two bath
-Three bedroom Two bath
all other information is on our current website
KEEP it simple and fresh
ALSO WE DONT HAVE HUGE BIG BOATS IN THE MARINA SO PLEASE DONT HAVE THAT IN THE LOGO

Target Market(s)

Anyone looking for accomodation !! we have 64 rooms !!

Industry/Entity Type

accomodation / short stays

Coding

Coded - Design and coding required

Number of Pages Required

5+ page

Requirements
Must have
• Fresh , modern and easy to use.....have a hoilday vibe , also use natural colours
Nice to have
• i like accomodation website like ....https://fernandgrove.com.au/luxury-coastal-accommodation/ or https://theorvellainn.com/
Should not have
• please do not use bright colours and scripted fonts

```html
<!DOCTYPE html>
<html lang="en">
<head>
<meta charset="utf-8">
<title>Tallowind Quay Residences — News &amp; Contact</title>
<link href="https://fonts.googleapis.com/css2?family=Jost:wght@300;400;500&display=swap" rel="stylesheet">
<style>
:root{
  --canvas:#ffffff;
  --paper:#fcfbf8;
  --band:#f8f7f3;
  --ink:#3a3a37;
  --muted:#8b887f;
  --faint:#b9b5ab;
  --line:#e9e6df;
  --dark:#1f1f1d;
  --field:#ffffff;
  --panel:#f6f5f1;
}
*{box-sizing:border-box;margin:0;padding:0}
html,body{width:1200px;height:1200px;overflow:hidden;background:var(--canvas)}
body{position:relative;font-family:'Jost',Helvetica,Arial,sans-serif;color:var(--ink);font-weight:300}
.page{position:absolute;width:782px;background:var(--paper);transform:scale(.621);transform-origin:0 0;box-shadow:0 0 0 1px #f1efea}
.page--news{left:108px;top:93px;height:1377px}
.page--contact{left:657px;top:93px;height:1020px}

/* header */
.site-header{position:absolute;left:0;top:0;width:100%;height:52px;border-bottom:1px solid var(--line)}
.brand{position:absolute;left:0;right:0;top:19px;text-align:center;line-height:1;color:var(--ink)}
.brand__name{display:block;font-size:7px;letter-spacing:.28em;font-weight:400}
.brand__sub{display:block;font-size:3px;letter-spacing:.4em;margin-top:2px;font-weight:400}
.nav{position:absolute;top:38px;left:0;right:0;display:flex;justify-content:center;gap:13px;font-size:3.4px;letter-spacing:.22em;color:var(--muted);text-transform:uppercase;padding-right:40px}
.nav__book{position:absolute;right:196px;top:-3px;border:1px solid var(--ink);color:var(--ink);padding:3px 9px;font-size:3.4px}

/* hero */
.hero{position:absolute;left:0;width:100%;height:292px;display:flex;flex-direction:column;align-items:center;justify-content:center;text-align:center;color:#fff}
.page--news .hero{top:52px;background:linear-gradient(180deg,#d9823a 0%,#c8763b 22%,#9b6a4c 40%,#7f6b5a 55%,#8b7f6d 72%,#5f6a4d 88%,#4c5a3e 100%)}
.page--contact .hero{top:56px;background:linear-gradient(180deg,#7b8aa3 0%,#a9a7ad 30%,#8a7a68 55%,#4e5a60 72%,#32515f 85%,#6b7a80 100%)}
.hero__eyebrow{font-size:3.2px;letter-spacing:.35em;text-transform:uppercase;opacity:.85;margin-bottom:6px;margin-top:22px}
.hero__title{font-size:11px;font-weight:300;letter-spacing:.12em;text-transform:uppercase}
.hero__lede{font-size:4px;max-width:150px;line-height:1.9;margin-top:8px;opacity:.9}

/* news grid */
.section-title{position:absolute;left:0;right:0;top:374px;text-align:center;font-size:9px;letter-spacing:.3em;font-weight:400;text-transform:uppercase}
.posts{position:absolute;left:194px;top:406px;width:392px;display:grid;grid-template-columns:repeat(4,84px);column-gap:18px;row-gap:0}
.post{height:239px}
.post__media{display:block;width:84px;height:127px}
.post__title{font-size:6px;letter-spacing:.1em;line-height:1.45;text-transform:uppercase;margin-top:8px;font-weight:300;color:var(--ink)}
.post__excerpt{font-size:3.6px;line-height:1.9;color:var(--muted);margin-top:5px}
.post__more{display:inline-block;font-size:3px;letter-spacing:.3em;color:var(--faint);margin-top:5px;text-transform:uppercase;border-bottom:1px solid var(--line);padding-bottom:1px}

/* contact */
.visit{position:absolute;left:217px;top:378px;width:120px;font-size:3.8px;line-height:1.8;color:var(--muted)}
.label{font-size:3px;letter-spacing:.3em;text-transform:uppercase;color:var(--faint);margin-bottom:3px}
.visit__row{display:flex;align-items:center;gap:4px;margin-top:4px}
.visit__row svg{width:5px;height:5px}
.visit__gap{height:7px}
.socials{display:flex;gap:4px;margin-top:9px}
.socials span{width:9px;height:9px;border:1px solid var(--line);border-radius:50%}
.enquiry{position:absolute;left:383px;top:378px;width:183px;height:183px;background:var(--panel);padding:13px 12px}
.enquiry__row{display:flex;gap:8px;margin-bottom:7px}
.field{flex:1}
.field .label{font-size:2.6px;margin-bottom:2px}
.field__box{height:13px;background:var(--field);border:1px solid var(--line);font-size:3px;color:var(--faint);padding:4px}
.field__box--tall{height:40px}
.send{display:inline-block;background:var(--dark);color:#fff;font-size:3.4px;padding:4px 10px;border-radius:8px;margin-top:4px}
.map{position:absolute;left:0;top:592px;width:100%;height:158px;background:linear-gradient(90deg,#e9ece6 0%,#e3e8e1 45%,#dfe6dc 60%,#a6d8ea 68%,#9dd4e8 100%)}

/* footer */
.footer{position:absolute;left:0;width:100%;bottom:0;background:var(--band);border-top:1px solid var(--line)}
.page--news .footer{top:1137px}
.page--contact .footer{top:780px}
.footer__cta{position:absolute;left:0;right:0;top:28px;text-align:center;font-size:5px;letter-spacing:.35em;text-transform:uppercase;font-weight:400}
.badges{position:absolute;left:0;right:0;top:49px;display:flex;justify-content:center;gap:12px}
.badges span{width:20px;height:9px;background:#d8d5cd;border-radius:2px}
.badges span:nth-child(2){border-radius:50%;width:11px}
.footer__rule{position:absolute;left:194px;right:194px;top:80px;border-top:1px solid var(--line)}
.footer__cols{position:absolute;left:196px;top:103px;width:392px;display:grid;grid-template-columns:repeat(4,101px);font-size:3.6px;line-height:1.9;color:var(--muted)}
.footer__brand{font-size:4.5px;letter-spacing:.3em;color:var(--ink);text-transform:uppercase;margin-bottom:6px;font-weight:400}
.footer__cols .label{margin-bottom:6px}
.footer__cols p{margin-bottom:3px}
.footer__note{font-size:3px;line-height:1.6;margin-top:3px}
.footer__links{text-transform:uppercase;letter-spacing:.25em;font-size:3px;line-height:2.6}
.footer__social{display:flex;gap:4px;margin-top:6px}
.footer__social span{width:10px;height:10px;border:1px solid var(--line)}
.footer__legal{position:absolute;left:196px;right:196px;bottom:25px;display:flex;justify-content:space-between;font-size:3px;letter-spacing:.3em;color:var(--faint);text-transform:uppercase}
</style>
</head>
<body>

<!-- News & Events page -->
<section class="page page--news">
  <header class="site-header">
    <div class="brand"><span class="brand__name">TALLOWIND QUAY</span><span class="brand__sub">RESIDENCES</span></div>
    <nav class="nav"><span>Home</span><span>About us</span><span>Accommodation</span><span>Our location</span><span>News &amp; Events</span><span>Contact us</span><span class="nav__book">Book</span></nav>
  </header>
  <div class="hero" role="img" aria-label="Sunset over the beach with a long jetty and headland, dune grasses in the foreground">
    <p class="hero__eyebrow">News &amp; Events</p>
    <h1 class="hero__title">Stories from the Marlow Coast</h1>
    <p class="hero__lede">Local guides, what's on, and the small details that make a Marlow getaway something to look forward to.</p>
  </div>

  <h2 class="section-title">Recent posts</h2>
  <div class="posts">
    <article class="post"><div class="post__media" role="img" aria-label="Humpback whale breaching near an island" style="background:linear-gradient(180deg,#c9d6e2,#4f7190 60%,#23405c)"></div><h3 class="post__title">The ultimate guide to whale watching on the Marlow Coast</h3><p class="post__excerpt">The Marlow Coast transforms into one of Australia's premier whale-watching destinations each year. Here's how to get the best experience.</p><span class="post__more">Read more</span></article>
    <article class="post"><div class="post__media" role="img" aria-label="Aerial view of waves on a rocky island coast" style="background:linear-gradient(160deg,#4d6a6a,#2c6f7c 50%,#1d4d63)"></div><h3 class="post__title">Walking on water: the Kestrel Islands coastal walk</h3><p class="post__excerpt">Few experiences capture the beauty of the Marlow Coast better than the Kestrel Islands Coastal Walk. Here's why it stands out.</p><span class="post__more">Read more</span></article>
    <article class="post"><div class="post__media" role="img" aria-label="Couple with coffee under an umbrella on a rainy day" style="background:linear-gradient(180deg,#e4ddd3,#9a6a4e 55%,#6e3a2c)"></div><h3 class="post__title">Fabulous wet weather indoor activities in Marlow Bay</h3><p class="post__excerpt">If the weather turns wet, visitors and locals can enjoy a variety of indoor activities that keep everyone entertained.</p><span class="post__more">Read more</span></article>
    <article class="post"><div class="post__media" role="img" aria-label="Golf ball on a green fairway with a golfer behind" style="background:linear-gradient(180deg,#d4e0e4,#7f9a66 50%,#5e8440)"></div><h3 class="post__title">A golfer's guide to the Marlow Coast</h3><p class="post__excerpt">The Marlow Coast offers some of Australia's most scenic and enjoyable golf courses — here are the standout courses worth teeing off on.</p><span class="post__more">Read more</span></article>

    <article class="post"><div class="post__media" role="img" aria-label="Traveller looking out from a balcony at the sea" style="background:linear-gradient(180deg,#a9bdd3,#7c8aa0 50%,#4a5060)"></div><h3 class="post__title">Accessible accommodation &amp; travel: exploring Marlow Bay</h3><p class="post__excerpt">Marlow Bay welcomes visitors with disabilities, with accessible beaches and experiences. Take a look at our accessible accommodation.</p><span class="post__more">Read more</span></article>
    <article class="post"><div class="post__media" role="img" aria-label="Harbour breakwall path with the marina behind" style="background:linear-gradient(180deg,#6f8fb8,#a0aab0 45%,#5a5e62)"></div><h3 class="post__title">Tallowind Quay: where comfort meets convenience</h3><p class="post__excerpt">Tallowind Quay Residences put you in the heart of everything that makes the Mid North Coast so special. Read on to find out why.</p><span class="post__more">Read more</span></article>
    <article class="post"><div class="post__media" role="img" aria-label="Bright white apartment interior with a sideboard" style="background:linear-gradient(180deg,#f2f1ef,#e3e1dc 60%,#cfccc5)"></div><h3 class="post__title">Explore our 1, 2 &amp; 3 bedroom apartments</h3><p class="post__excerpt">Marlow is a fabulous destination — natural beauty and endless family adventures. Tallowind Quay is the perfect base.</p><span class="post__more">Read more</span></article>
    <article class="post"><div class="post__media" role="img" aria-label="Apartment building exterior with tropical garden" style="background:linear-gradient(180deg,#a5b9cc,#5d6a66 45%,#3f5a3a)"></div><h3 class="post__title">Experience Marlow Bay</h3><p class="post__excerpt">The Marlow Coast delivers unforgettable moments — and Tallowind Quay Residences are your stylish base from which to experience it all.</p><span class="post__more">Read more</span></article>

    <article class="post"><div class="post__media" role="img" aria-label="Business traveller relaxing in an apartment lounge" style="background:linear-gradient(180deg,#c7b59a,#7a6a58 50%,#3d3a36)"></div><h3 class="post__title">Marlow Bay: where business meets pleasure</h3><p class="post__excerpt">Marlow Bay blends business opportunities with a relaxed coastal lifestyle — the perfect location for business travel and a getaway.</p><span class="post__more">Read more</span></article>
    <article class="post"><div class="post__media" role="img" aria-label="Beer being poured from a brewery tap" style="background:linear-gradient(180deg,#c4c8cc,#a39a8a 50%,#b8782e)"></div><h3 class="post__title">Craft beer &amp; coastal vibes: your guide to Marlow Coast breweries</h3><p class="post__excerpt">Fancy a cold one with a side of Marlow Bay's laid-back charm? Take our Marlow Coast Breweries tour for an awesome day out.</p><span class="post__more">Read more</span></article>
  </div>

  <footer class="footer">
    <p class="footer__cta">Book direct and save</p>
    <div class="badges"><span></span><span></span><span></span></div>
    <div class="footer__rule"></div>
    <div class="footer__cols">
      <div><p class="footer__brand">Tallowind Quay</p><p>Accredited 4-star self-contained apartments in the heart of the Marlow Bay Jetty Precinct.</p></div>
      <div><p class="label">Contact</p><p>14 Wattlebird Street<br>Marlow Bay NSW 2999</p><p>1800 555 014</p><p>sales@tallowindquay.com.au</p></div>
      <div><p class="label">Reception hours</p><p>Mon – Fri · 9am to 5pm</p><p>Saturday · 10am to 2pm</p><p>Sunday · 9am to 4pm</p><p class="footer__note">After hours: leave a message and we'll respond within 24 hours.</p></div>
      <div><p class="label">Visit</p><div class="footer__links">About us<br>Accommodation<br>Our location<br>News &amp; Events<br>Contact us</div><div class="footer__social"><span></span><span></span></div></div>
    </div>
    <div class="footer__legal"><span>© 2026 Tallowind Quay Residences</span><span>14 Wattlebird Street · Marlow Bay NSW</span></div>
  </footer>
</section>

<!-- Contact page -->
<section class="page page--contact">
  <header class="site-header">
    <div class="brand"><span class="brand__name">TALLOWIND QUAY</span><span class="brand__sub">RESIDENCES</span></div>
    <nav class="nav"><span>Home</span><span>About us</span><span>Accommodation</span><span>Our location</span><span>News &amp; Events</span><span>Contact us</span><span class="nav__book">Book</span></nav>
  </header>
  <div class="hero" role="img" aria-label="Old timber jetty stretching out over the sea at dusk">
    <h1 class="hero__title" style="margin-top:90px">Say hello</h1>
    <p class="hero__lede" style="max-width:190px">Have a question about your stay, our apartments or the Marlow Coast? Drop us a line — we'd love to hear from you.</p>
  </div>

  <div class="visit">
    <p class="label">Visit</p>
    <p>Tallowind Quay Residences<br>Marlow Bay NSW 2999<br>Australia</p>
    <div class="visit__gap"></div>
    <div class="visit__row"><svg viewBox="0 0 10 10"><path d="M2 1l2 0 1 2.5-1.3 1a6 6 0 0 0 2.8 2.8l1-1.3 2.5 1v2a1 1 0 0 1-1 1A8 8 0 0 1 1 2a1 1 0 0 1 1-1z" fill="none" stroke="#6b6962" stroke-width="1"/></svg>+61 2 5550 0142</div>
    <div class="visit__row"><svg viewBox="0 0 10 10"><rect x="1" y="2" width="8" height="6" fill="none" stroke="#6b6962" stroke-width="1"/><path d="M1 2l4 3.5L9 2" fill="none" stroke="#6b6962" stroke-width="1"/></svg>stay@tallowindquay.com.au</div>
    <div class="socials"><span></span><span></span></div>
  </div>

  <form class="enquiry">
    <div class="enquiry__row"><div class="field"><p class="label">Name</p><div class="field__box"></div></div><div class="field"><p class="label">Email</p><div class="field__box"></div></div></div>
    <div class="enquiry__row"><div class="field"><p class="label">Phone</p><div class="field__box"></div></div></div>
    <div class="enquiry__row"><div class="field"><p class="label">Dates of stay</p><div class="field__box">e.g. 12 – 16 March</div></div></div>
    <div class="enquiry__row"><div class="field"><p class="label">Message</p><div class="field__box field__box--tall"></div></div></div>
    <span class="send">Send enquiry</span>
  </form>

  <div class="map" role="img" aria-label="Street map of Marlow Bay showing the apartments near the jetty and harbour"></div>

  <footer class="footer">
    <p class="footer__cta">Book direct and save</p>
    <div class="badges"><span></span><span></span><span></span></div>
    <div class="footer__rule"></div>
    <div class="footer__cols">
      <div><p class="footer__brand">Tallowind Quay</p><p>Accredited 4-star self-contained apartments in the heart of the Marlow Bay Jetty Precinct.</p></div>
      <div><p class="label">Contact</p><p>14 Wattlebird Street<br>Marlow Bay NSW 2999</p><p>1800 555 014</p><p>sales@tallowindquay.com.au</p></div>
      <div><p class="label">Reception hours</p><p>Mon – Fri · 9am to 5pm</p><p>Saturday · 10am to 2pm</p><p>Sunday · 9am to 4pm</p><p class="footer__note">After hours: leave a message and we'll respond within 24 hours.</p></div>
      <div><p class="label">Visit</p><div class="footer__links">About us<br>Accommodation<br>Our location<br>News &amp; Events<br>Contact us</div><div class="footer__social"><span></span><span></span></div></div>
    </div>
    <div class="footer__legal"><span>© 2026 Tallowind Quay Residences</span><span>14 Wattlebird Street · Marlow Bay NSW</span></div>
  </footer>
</section>

</body>
</html>
```